Business Card Design Project

Personal Service. There are three areas of my service: Resourceful/Recycling Consultation, Life Coaching using Law of Attraction & Visualization Board. My current cards has: Vision Into Being. I would like to work with this theme

Industry/Entity Type

Business

Contact Information for Business Card

Circles. Recyling Triangle

```html
<!DOCTYPE html>
<html lang="en">
<head>
<meta charset="utf-8">
<title>Vision Into Being – Business Card</title>
<link href="https://fonts.googleapis.com/css2?family=Oswald:wght@400;600&family=Open+Sans:wght@400&display=swap" rel="stylesheet">
<style>
  :root {
    --page: #ececec;
    --card: #fbfbfb;
    --ink: #3a3a3a;
    --brand-blue: #2b87b1;
    --brand-green: #79b52b;
    --on-blue: #ffffff;
  }
  * { margin: 0; padding: 0; box-sizing: border-box; }
  html, body {
    width: 1200px; height: 900px; overflow: hidden;
    background: var(--page);
  }
  .card {
    position: absolute; left: 130px; top: 159px;
    width: 940px; height: 582px;
    background: var(--card);
    box-shadow: 0 6px 24px rgba(0,0,0,.12);
    overflow: hidden;
  }
  .card__panel {
    position: absolute; inset: 0; width: 100%; height: 100%;
  }
  .brand {
    position: absolute; left: 53px; top: 101px; width: 443px;
    display: flex; flex-direction: column; align-items: center;
  }
  .brand__dot {
    width: 110px; height: 110px; border-radius: 50%;
    background: var(--brand-blue);
    margin-bottom: 42px;
  }
  .brand__name {
    font-family: "Oswald", sans-serif; font-weight: 600;
    font-size: 40px; letter-spacing: .5px; line-height: 1;
    color: var(--ink); text-transform: uppercase; white-space: nowrap;
  }
  .services {
    position: absolute; left: 63px; top: 367px;
    list-style: none;
    font-family: "Open Sans", sans-serif; font-size: 23.5px;
    line-height: 34px; color: var(--ink);
  }
  .services li { position: relative; padding-left: 16px; }
  .services li::before {
    content: ""; position: absolute; left: -2px; top: 11px;
    width: 13px; height: 13px; border-radius: 50%;
    background: var(--brand-blue);
  }
  .contact {
    position: absolute; right: 46px; top: 0;
    text-align: right; color: var(--on-blue);
    font-family: "Open Sans", sans-serif;
  }
  .contact__name {
    position: absolute; right: 0; top: 192px;
    font-family: "Oswald", sans-serif; font-weight: 400;
    font-size: 45px; line-height: 50px; white-space: nowrap;
    text-transform: uppercase;
  }
  .contact__role {
    position: absolute; right: 0; top: 247px;
    font-size: 24px; line-height: 30px; white-space: nowrap;
  }
  .contact__lines {
    position: absolute; right: 0; top: 315px;
    list-style: none; font-size: 23.5px; line-height: 34.5px;
  }
  .contact__lines li {
    display: flex; justify-content: flex-end; align-items: center;
    gap: 8px; white-space: nowrap;
  }
  .contact__lines svg { width: 20px; height: 20px; fill: var(--on-blue); }
  .contact__address {
    position: absolute; right: 0; top: 444px;
    font-size: 23.5px; line-height: 33px; white-space: nowrap;
  }
</style>
</head>
<body>
  <div class="card">
    <svg class="card__panel" viewBox="0 0 652 404" preserveAspectRatio="none" aria-hidden="true">
      <path d="M550,0 C430,78 300,250 287,404 L652,404 L652,0 Z" fill="var(--brand-blue)"/>
      <path d="M550,0 C426,78 292,250 282,404" fill="none" stroke="var(--brand-green)" stroke-width="3"/>
    </svg>

    <div class="brand">
      <span class="brand__dot"></span>
      <span class="brand__name">Vision Into Being</span>
    </div>

    <ul class="services">
      <li>Resourceful/<br>Recycling Consultation</li>
      <li>Life Coaching using Law<br>of Attraction</li>
      <li>Visualization Board</li>
    </ul>

    <div class="contact">
      <h1 class="contact__name">Daniel Marsh</h1>
      <p class="contact__role">Managing Director</p>
      <ul class="contact__lines">
        <li>044-987 654 321
          <svg viewBox="0 0 20 20"><path d="M2 8c0-3 3-5 8-5s8 2 8 5l-3 1-1-2c-2-1-6-1-8 0L5 9zM5 10h10l2 6H3z"/></svg>
        </li>
        <li>044-987 654 321
          <svg viewBox="0 0 20 20"><path d="M6 1h8a1 1 0 0 1 1 1v16a1 1 0 0 1-1 1H6a1 1 0 0 1-1-1V2a1 1 0 0 1 1-1zm1 2v12h6V3zm3 13.2a1 1 0 1 0 0 .1z"/></svg>
        </li>
        <li>hello@sitename.com
          <svg viewBox="0 0 20 20"><path d="M2 4h16v12H2zm1.5 1.5 6.5 5 6.5-5z"/></svg>
        </li>
      </ul>
      <p class="contact__address">48 Harbour Lane, Westbury<br>Northland, 204518</p>
    </div>
  </div>
</body>
</html>
```